Brisvale app design refresh: 1 new screen, 1 new icon / 11 icons reworked for hi-res, addtnl elements

UPDATE: added task 6

I have a ready design for the app that needs to be updated, but my previous designer can't help due to the workload.

Tasks which need to be accomplished:
1) new Tutorial icon - we used question mark in a
circle for Tutorial request, but I need something different now, because Tutorials are more about assistance than help in a traditional sense; I am thinking about pencil or graduation hat icons, but am open to other ideas
2) guidance on control elements: when you first open Journal screen you should see the bubble around the '+' icon with the text 'Start Here' inside - I need this bubble with text (shape, color etc.)
3) new Tutorial screen - half-transparent dark layer over the screen, where you see the name of the step than some formatted text plus Populate and Continue buttons at the bottom
4) the icons should be reworked for high resolution screens (6 and 6+) - including keyboard, letter A, icons inside the text formatting panel, tag, export, delete (especially keyboard icon)
5) I want one more color introduced for text - now we have only white and black/grey; for example I want the title of the step look different from the text, different color; so, just give me another color which would look great with existing palette
6) Icon for Summary functionality needs to be created; Archive with appropriate themes is attached

Attached is the existing design for Norvex 4s. Your target design should be for 4s and 5/5s and 6/6+

• 4/4s/5/5s/6/6+ quality

```html
<!DOCTYPE html>
<html lang="en">
<head>
<meta charset="utf-8">
<title>Brisvale – Tutorial Screen</title>
<link href="https://fonts.googleapis.com/css2?family=Open+Sans:wght@300;400;600&display=swap" rel="stylesheet">
<style>
  :root {
    --page: #f4f5f6;
    --screen: #2b3035;
    --screen-text: #3d444b;
    --overlay: rgba(28, 32, 36, 0.55);
    --ink-light: #ffffff;
    --ink-dark: #33383d;
    --accent: #63b8ab;
    --lens: #ffffff;
  }
  * { box-sizing: border-box; margin: 0; padding: 0; }
  html, body {
    width: 1200px; height: 900px; overflow: hidden;
    background: var(--page);
    font-family: "Open Sans", sans-serif;
  }
  .screen {
    position: absolute; left: 390px; top: 50px;
    width: 420px; height: 800px;
    background: var(--screen);
    overflow: hidden;
  }
  .status-bar {
    height: 26px; padding: 0 14px;
    display: flex; align-items: center; justify-content: center;
    font-size: 12px; color: var(--screen-text); font-weight: 600;
  }
  .header {
    height: 58px; display: flex; align-items: center; justify-content: center;
    font-size: 22px; font-weight: 300; color: var(--screen-text);
    border-bottom: 1px solid #343a40;
  }
  .body-text {
    padding: 20px 24px; font-size: 13px; line-height: 19px;
    color: var(--screen-text);
  }
  .body-text p { margin-bottom: 16px; }
  .overlay { position: absolute; inset: 0; background: var(--overlay); }
  .close {
    position: absolute; right: 18px; top: 38px; width: 22px; height: 22px;
  }
  .lens {
    position: absolute; width: 118px; height: 118px; border-radius: 50%;
    background: var(--lens); overflow: hidden;
    font-size: 16px; line-height: 22px; color: var(--ink-dark);
    padding: 0 6px;
  }
  .lens-title { padding-top: 30px; border-top: 14px solid var(--accent); }
  .lens-title span { display: block; border-bottom: 1px solid #d8dcdf; padding-bottom: 8px; }
  .lens-body { padding-top: 14px; white-space: nowrap; }
  .lens-body p + p { margin-top: 8px; }
  .tip {
    position: absolute; color: var(--ink-light);
    font-size: 19px; line-height: 25px; font-weight: 400;
  }
  .continue-bar {
    position: absolute; left: 0; right: 0; bottom: 0; height: 150px;
    background: var(--accent);
    display: flex; align-items: center; justify-content: center;
  }
</style>
</head>
<body>
  <main class="screen">
    <div class="status-bar">9:41 PM</div>
    <div class="header">Step A</div>
    <div class="body-text">
      <p>We worked on the new layout for the first few weeks of our plan and then moved on to the next step with a clear goal.</p>
      <p>Each of us had a short note to share with the team at the end of the day.</p>
      <p>Lorem ipsum dolor sit amet, at tale sophia usu, quo enim homero ut. Duo ex ponderum accusata, ei modus option qui.</p>
    </div>

    <div class="overlay"></div>

    <svg class="close" viewBox="0 0 22 22" aria-label="Close">
      <path d="M3 3 L19 19 M19 3 L3 19" stroke="#ffffff" stroke-width="2" stroke-linecap="round"/>
    </svg>

    <div class="lens" style="left:28px; top:74px;">
      <div class="lens-title"><span>Title of the</span></div>
    </div>
    <p class="tip" style="left:162px; top:112px; width:220px;">Add title here, anything you want.</p>

    <div class="lens" style="left:88px; top:250px;">
      <div class="lens-body" style="margin-left:-10px;">
        <p>of us had</p>
        <p>sum dolor sit a</p>
        <p>ent team at,</p>
      </div>
    </div>
    <p class="tip" style="left:222px; top:272px; width:170px;">Create 532 words with great explina-tions.</p>

    <div class="lens" style="left:262px; top:450px;">
      <div class="lens-body">
        <p>ophia usu,</p>
        <p>quo enim hin</p>
      </div>
    </div>
    <p class="tip" style="left:40px; top:462px; width:210px;">Dont forget to add spacing in sentences you add.</p>

    <div class="continue-bar">
      <svg width="16" height="18" viewBox="0 0 16 18" aria-label="Continue">
        <path d="M8 2 V15 M3 10 L8 15 L13 10" stroke="#ffffff" stroke-width="2" fill="none" stroke-linecap="round" stroke-linejoin="round"/>
      </svg>
    </div>
  </main>
</body>
</html>
```